Sport Celebration Day Poster

The poster should highlight the sport of archery and bring awareness to the sport and invite people to come and try archery. We have a logo that must be featured, as well as a sample photos that can be used in the creative process, but do not necessarily have to be featured. The feel of the poster should be fun and inviting and have archery imagery (bows, arrows, targets, etc.).

The poster must feature the date MAY 11, 2019 and "Try Archery."

We would like to see an area where our sport clubs can fill in their own information including sections for "Name, Date, Location, Times, Location, Email, Website, and Notes."

Submissions should include some of these colours or colours from the logo:
Blue #00A1EF, Grey #313A43, Green #406C1D, Red #DC2F31, Yellow #FDDD39

```html
<!DOCTYPE html>
<html lang="en">
<head>
<meta charset="utf-8">
<title>Try Archery – May 11, 2019</title>
<link rel="stylesheet" href="https://fonts.googleapis.com/css2?family=Titan+One&family=Comic+Neue:wght@700&family=Open+Sans:wght@600;700&display=swap">
<style>
  :root {
    --page: #e4e4e2;
    --blue: #1f5fbf;
    --red: #c8202a;
    --red-deep: #b01c24;
    --mint: #d6f6ea;
    --teal: #8fd9cf;
    --sky: #5fbdd2;
    --hill: #4aa6c4;
    --grass: #5ea733;
    --cloud: #eceef0;
    --cloud-edge: #c9cdd1;
    --ink: #c8202a;
    --white: #ffffff;
    --badge: #b8bcc0;
    --archer-warm: #e59a55;
    --archer-cool: #3f5f9a;
  }
  * { box-sizing: border-box; margin: 0; padding: 0; }
  html, body { width: 1200px; height: 960px; overflow: hidden; background: var(--page); }
  .poster {
    position: absolute; left: 282px; top: 30px; width: 636px; height: 900px;
    background: var(--white); overflow: hidden;
    box-shadow: 0 6px 24px rgba(0,0,0,.18);
  }
  .scene {
    position: absolute; left: 0; top: 0; width: 636px; height: 835px;
    background: linear-gradient(180deg, var(--white) 0%, var(--mint) 12%, var(--teal) 40%, var(--sky) 55%, var(--hill) 76%, var(--grass) 84%, var(--grass) 100%);
  }
  .archer {
    position: absolute; left: 22px; top: 508px; width: 196px; height: 255px;
    border-radius: 40px 40px 12px 12px;
    background: linear-gradient(180deg, var(--archer-warm) 0%, var(--archer-warm) 40%, var(--archer-cool) 100%);
    opacity: .85;
  }
  .target {
    position: absolute; left: 440px; top: 522px; width: 132px; height: 240px;
    border-radius: 60px 60px 8px 8px;
    background: linear-gradient(180deg, var(--red) 0%, var(--white) 45%, var(--red) 70%, #7a4a2a 100%);
    opacity: .85;
  }
  .logo { position: absolute; display: flex; align-items: center; gap: 6px; z-index: 3;
    font-family: "Open Sans", sans-serif; font-weight: 700; color: var(--red); }
  .logo-event { left: 18px; top: 34px; font-size: 20px; }
  .logo-federation { right: 22px; top: 32px; font-size: 20px; }
  .logo .mark { width: 18px; height: 18px; border-radius: 50%; background: var(--red); }
  .headline { position: absolute; left: 0; top: 0; width: 636px; height: 900px; pointer-events: none; z-index: 2; }
  .headline text { font-family: "Titan One", sans-serif; fill: var(--blue);
    stroke: var(--red); stroke-width: 8; paint-order: stroke; stroke-linejoin: round; }
  .tag { position: absolute; z-index: 1; }
  .tag svg { position: absolute; inset: 0; width: 100%; height: 100%; overflow: visible; }
  .tag .cord { position: absolute; left: 50%; bottom: 100%; width: 1px; height: 140px; background: rgba(255,255,255,.6); }
  .tag p { position: relative; height: 100%; display: flex; flex-direction: column; justify-content: center;
    text-align: center; font-family: "Comic Neue", cursive; font-weight: 700; color: var(--ink); line-height: 1.2; }
  .tag-equipment { left: 10px; top: 240px; width: 140px; height: 84px; }
  .tag-equipment p { font-size: 15px; padding-top: 6px; }
  .tag-family { left: 402px; top: 272px; width: 180px; height: 108px; }
  .tag-family p { font-size: 16px; padding-top: 8px; }
  .tag-experience { left: 40px; top: 392px; width: 94px; height: 74px; }
  .tag-experience p { font-size: 11px; padding-top: 8px; }
  .tag-details { left: 146px; top: 345px; width: 290px; height: 190px; }
  .tag-details p { align-items: flex-start; padding: 28px 0 0 42px; font-size: 18px; line-height: 1.3; text-align: left; }
  .notices { position: absolute; left: 158px; top: 764px; width: 332px; height: 56px; z-index: 2;
    background: var(--red); border: 2px solid var(--white); border-radius: 8px 8px 0 0; }
  .notices h2 { position: absolute; left: 100px; top: -18px; width: 110px; height: 26px;
    background: var(--red-deep); border: 2px solid var(--white); border-radius: 6px;
    font-family: "Open Sans", sans-serif; font-weight: 600; font-size: 18px; line-height: 21px;
    color: var(--white); text-align: center; }
  .footer { position: absolute; left: 0; top: 820px; width: 636px; height: 80px; z-index: 2;
    background: var(--white); border-top: 4px solid var(--red); }
  .partners { position: absolute; left: 40px; top: 18px; display: flex; gap: 22px; align-items: center; }
  .partners span { display: block; width: 44px; height: 26px; background: var(--badge); border-radius: 4px; }
  .contact { position: absolute; left: 392px; top: 16px; font-family: "Open Sans", sans-serif;
    font-weight: 700; font-size: 13px; color: var(--red); line-height: 1.3; }
</style>
</head>
<body>
<svg width="0" height="0" style="position:absolute">
  <defs>
    <symbol id="cloud-shape" viewBox="0 0 200 120" preserveAspectRatio="none">
      <path d="M30,108 C4,108 2,70 28,66 C20,36 56,22 74,40 C82,10 128,8 136,36 C154,20 190,36 178,64 C200,70 198,108 172,108 Z"
            fill="var(--cloud)" stroke="var(--cloud-edge)" stroke-width="2"/>
      <circle cx="100" cy="22" r="4" fill="var(--hill)"/>
    </symbol>
  </defs>
</svg>

<main class="poster">
  <div class="scene" role="img" aria-label="Cartoon landscape with soft clouds, blue hills and green grass"></div>
  <div class="archer" role="img" aria-label="Cartoon girl drawing a red recurve bow, quiver of arrows on her hip"></div>
  <div class="target" role="img" aria-label="Red and white archery target on a wooden stand with an arrow in the centre"></div>

  <div class="logo logo-event"><span class="mark"></span>Bullseye Day</div>
  <div class="logo logo-federation"><span class="mark"></span>Northbow Archery</div>

  <div class="tag tag-equipment">
    <span class="cord"></span>
    <svg><use href="#cloud-shape"/></svg>
    <p>All equipments<br>Provided</p>
  </div>
  <div class="tag tag-family">
    <span class="cord"></span>
    <svg><use href="#cloud-shape"/></svg>
    <p>Perfect<br>activity for the<br>whole family</p>
  </div>
  <div class="tag tag-experience">
    <svg><use href="#cloud-shape"/></svg>
    <p>No Experience<br>required</p>
  </div>
  <div class="tag tag-details">
    <span class="cord"></span>
    <svg><use href="#cloud-shape"/></svg>
    <p>Name:<br>Date:<br>Location:<br>Times:</p>
  </div>

  <svg class="headline" viewBox="0 0 636 900" aria-label="Try Archery! May 11, 2019">
    <defs>
      <path id="arc-title" d="M62,212 Q290,40 540,176"/>
      <path id="arc-date" d="M178,268 Q320,190 470,238"/>
    </defs>
    <text font-size="62"><textPath href="#arc-title">Try Archery!</textPath></text>
    <text font-size="34"><textPath href="#arc-date">MAY 11, 2019</textPath></text>
  </svg>

  <section class="notices"><h2>Notices</h2></section>

  <footer class="footer">
    <div class="partners"><span></span><span></span><span></span></div>
    <div class="contact">Email:<br>Website:</div>
  </footer>
</main>
</body>
</html>
```